Need a Wordpress website for my HVAC company

I need a Wordpress website created for an HVAC company in a competitive market.
Following are some websites I like:
My current website is www.brovikclimate.com - we also have a facebook page with some pictures

We are an airconditioning and heating company that does both residential and commmercial work.
We need the following info on our website:
-mobile friendly
-Schedule an appt -repair/maintnenace/installation (i would like this option to always be on the page even if they scroll down.)
-24 hour service
-coupons /promotions
-financing
-reviews/testimonials
-about
-blog
-Our service area
The following are services we provide:
-Air conditioning - Installation/Service/Maintenance/new construction
-Heating - Installation/Service/Maintenance/new construction ( gas furnace, 2 stage furnace, electric heat)
-Duct - Repair/Replacement/Istallation - (zone systems)
-thermostats (wifi)
-Heat pump
-Air handler
-self communicating systems
-carbon monoxide testing
-hail damage
-duct sealing
-insulation
-Air cleaners - UV Air purifiers
-humidifiers

I would also like Quillo SEO add on

Target Market(s)

Anyone who needs our services HVAC contractor

Industry/Entity Type

Hvac

Contact Information for Business Card

Phone:480-555-2064
website:www.brovikclimate.com
email pmarsh@brovikclimate.com

Coding

Coded - Design and coding required

Number of Pages Required

5+ page

Font styles to use
Serif
Sans Serif

Requirements
Must have
• I wrote in brief. I already have Nimbo Vault. Long story I paid for 3 years already. I need someone to put website there. Ive never used Wordpress but would like a template page so I can easily add services.
Nice to have
• Clean, bright, original

```html
<!DOCTYPE html>
<html lang="en">
<head>
<meta charset="utf-8">
<title>Brovik Climate Services – Heating &amp; Air Conditioning</title>
<link rel="stylesheet" href="https://fonts.googleapis.com/css2?family=Lato:ital,wght@0,400;0,700;0,900;1,400&family=Roboto:wght@400;500;700&display=swap">
<style>
:root{
  --navy:#163c63;
  --blue:#1c5a8f;
  --blue-bright:#2a74b3;
  --green:#23865a;
  --green-dark:#1b6d48;
  --red:#c9252c;
  --ink:#333;
  --muted:#555;
  --grey-bg:#efefef;
  --light:#f6f6f6;
  --footer:#1d2530;
  --white:#fff;
}
*{box-sizing:border-box;margin:0;padding:0}
html,body{width:1200px;height:3863px;overflow:hidden}
body{position:relative;font-family:"Lato",Arial,sans-serif;color:var(--ink);background:var(--white)}
.abs{position:absolute}
.sec{position:absolute;left:0;width:1200px}
.btn{position:absolute;display:inline-flex;align-items:center;gap:12px;height:40px;padding:0 8px 0 26px;border-radius:20px;color:#fff;font:700 14px "Roboto",sans-serif;letter-spacing:.5px;text-transform:uppercase}
.btn .arr{width:26px;height:26px;border-radius:50%;background:#fff;display:flex;align-items:center;justify-content:center}
.btn-red{background:var(--red)}
.btn-navy{background:var(--navy)}
.btn-green{background:var(--green)}
.title{position:absolute;left:0;width:1200px;text-align:center;font:700 32px "Roboto",sans-serif;text-transform:uppercase;letter-spacing:.5px;color:var(--blue)}
.title em{font-style:normal;color:var(--green)}
.lorem{font-size:15px;line-height:24px;color:var(--muted)}

/* top bar */
.topbar{top:0;height:44px;background:var(--navy);color:#fff;font-size:13px}
.topbar .call{left:82px;top:13px;display:flex;gap:10px;align-items:center}
.dot-ic{width:22px;height:22px;border-radius:50%;background:var(--red);display:inline-flex;align-items:center;justify-content:center}
.topbar .quick{right:82px;top:11px;display:flex;gap:28px}
.topbar .quick span{display:flex;gap:8px;align-items:center}

/* nav */
.nav{top:44px;height:141px;background:#fff}
.nav a{position:absolute;top:62px;font:700 15px "Lato",sans-serif;color:#222;text-decoration:none}
.nav a.active{color:var(--red)}
.brand{left:490px;top:6px;width:220px;height:150px;display:flex;flex-direction:column;align-items:center;justify-content:center;gap:10px;background:#fff;border-radius:0 0 12px 12px;z-index:3}
.brand .mark{width:62px;height:62px;border-radius:50%;background:var(--blue)}
.brand .name{font:700 22px "Roboto",sans-serif;color:var(--blue);text-align:center;line-height:24px}
.dropdown{left:304px;top:149px;width:515px;height:263px;background:rgba(255,255,255,.96);border-top:4px solid var(--red);z-index:4;box-shadow:0 4px 10px rgba(0,0,0,.15);font-size:13px}
.dropdown ul{position:absolute;top:10px;list-style:none;width:230px}
.dropdown li{height:33px;line-height:33px;padding-left:14px;color:#333}
.dropdown li.on{background:var(--blue);color:#fff}
.dropdown li::before{content:"» ";color:#999}

/* hero */
.hero{top:185px;height:479px;background:linear-gradient(180deg,#9cb9d2 0%,#cbd7de 30%,#8c9a86 65%,#5f7a4e 100%)}
.hero-box{left:103px;top:111px;width:412px;height:225px;background:rgba(20,30,40,.55);padding:24px 10px}
.hero-box h1{font:700 26px/36px "Roboto",sans-serif;color:#fff}
.hero .dots{left:113px;top:343px;display:flex;gap:8px}
.hero .dots i{width:14px;height:14px;border-radius:50%;border:2px solid #fff;background:transparent}
.hero .dots i.on{background:var(--green)}

/* welcome */
.welcome{top:664px;height:340px}
.welcome p{position:absolute;left:100px;width:1000px;top:134px;text-align:center}

/* services */
.services{top:1004px;height:683px;background:var(--grey-bg)}
.tab{position:absolute;left:450px;top:0;width:300px;height:54px;background:#fff;clip-path:polygon(0 0,100% 0,90% 100%,10% 100%)}
.svc{position:absolute;width:490px;display:flex;gap:20px}
.svc .ic{flex:none;width:108px;height:108px;border-radius:50%;border:3px solid var(--blue);display:flex;align-items:center;justify-content:center;background:#fff}
.svc h3{font:700 17px "Roboto",sans-serif;color:var(--blue);margin:20px 0 4px}
.svc p{font-size:13px;line-height:17px;color:var(--muted)}

/* satisfaction */
.satisfy{top:1687px;height:291px}
.satisfy h2{position:absolute;left:0;width:1000px;text-align:center;top:60px;font:400 40px/56px "Roboto",sans-serif;color:#111;text-transform:uppercase}

/* promos */
.promo{top:1978px;height:358px}
.half{position:absolute;top:0;width:600px;height:358px;text-align:center;color:#fff}
.half .circ{position:absolute;left:244px;top:30px;width:112px;height:112px;border-radius:50%;background:#fff;border:4px solid var(--green);display:flex;align-items:center;justify-content:center}
.half h3{position:absolute;top:160px;width:600px;font:700 22px "Roboto",sans-serif}
.half p{position:absolute;left:120px;width:360px;top:200px;font-size:13px;line-height:17px}

/* testimonials */
.testi{top:2336px;height:497px}
.testi p{position:absolute;left:100px;width:1000px;top:176px;text-align:center}
.avatar{left:572px;top:316px;width:56px;height:56px;border-radius:50%;background:linear-gradient(#c9b8a6,#8e7b6a);border:2px solid #ddd}
.testi .who{position:absolute;width:1200px;text-align:center;top:390px;font:700 17px "Lato",sans-serif}
.testi .role{position:absolute;width:1200px;text-align:center;top:416px;font:italic 13px "Lato",sans-serif;color:#666}
.tdots{left:569px;top:450px;display:flex;gap:10px}
.tdots i{width:10px;height:10px;border-radius:50%;background:var(--green)}
.tdots i.off{background:#bbb}

/* blogs */
.blogs{top:2833px;height:553px;background:var(--light)}
.card{position:absolute;top:136px;width:330px;height:371px;background:#fff;box-shadow:0 1px 4px rgba(0,0,0,.1)}
.card .ph{height:180px}
.card .date{position:absolute;left:0;top:0;width:58px;height:112px;background:var(--blue);color:#fff;text-align:center;padding-top:10px;font:400 14px/20px "Lato",sans-serif}
.card .date b{display:block;font-size:22px;line-height:28px}
.card h4{margin:24px 16px 8px;font:700 15px "Roboto",sans-serif;color:#111}
.card p{margin:0 16px;font-size:13px;line-height:17px;color:var(--muted)}
.card .meta{position:absolute;left:16px;right:16px;bottom:16px;border-top:1px solid #e3e3e3;padding-top:12px;font-size:12px;color:#444}

/* footer */
.footer{top:3386px;height:477px;background:linear-gradient(180deg,#16202b,#26303c 60%,#1a222b)}
.fc{position:absolute;top:44px;width:300px;text-align:center;color:#fff;font-size:12px}
.fc .line{position:absolute;top:14px;height:1px;background:var(--green);width:96px}
.fc span{display:block;margin-top:22px}
.fnav{position:absolute;left:0;width:1200px;top:334px;display:flex;justify-content:center;gap:70px;color:#fff;font-size:14px}
.frule{left:82px;top:372px;width:1036px;height:1px;background:rgba(255,255,255,.25)}
.copy{left:82px;top:432px;font-size:12px;color:#ddd}
.social{right:82px;top:418px;display:flex;gap:12px}
.social i{width:34px;height:34px;border-radius:50%;background:var(--blue-bright)}
.social i.r{background:var(--red)}
</style>
</head>
<body>

<header class="sec topbar">
  <div class="abs call"><span class="dot-ic"><svg width="12" height="12" viewBox="0 0 24 24"><path fill="#fff" d="M6.6 10.8a15 15 0 0 0 6.6 6.6l2.2-2.2c.3-.3.7-.4 1-.2 1.1.4 2.3.6 3.6.6.6 0 1 .4 1 1V20c0 .6-.4 1-1 1A17 17 0 0 1 3 4c0-.6.4-1 1-1h3.5c.6 0 1 .4 1 1 0 1.3.2 2.5.6 3.6.1.3 0 .7-.2 1z"/></svg></span>Call (480) 555-2064 24 hours a day · 7 days a week</div>
  <div class="abs quick">
    <span><i class="dot-ic"></i>Repair</span>
    <span><i class="dot-ic"></i>Maintenance</span>
    <span><i class="dot-ic"></i>Installation</span>
  </div>
</header>

<nav class="sec nav">
  <a class="active" style="left:82px">Home</a>
  <a style="left:180px">About Us</a>
  <a style="left:300px;color:var(--red)">Services</a>
  <a style="left:430px">Blog</a>
  <a style="left:808px">Financing</a>
  <a style="left:922px">Testimonials</a>
  <a style="left:1058px">Contact Us</a>
  <div class="abs brand"><div class="mark"></div><div class="name">Brovik Climate</div></div>
</nav>

<div class="abs dropdown">
  <ul style="left:8px">
    <li>Air Conditioning</li><li>Heating</li><li>Thermostats</li><li class="on">Heat Pump</li><li>Air Handler</li><li>Self Communicating Systems</li><li>Carbon Monoxide Testing</li>
  </ul>
  <ul style="left:262px">
    <li>Hail Damage</li><li>Duct Sealing</li><li>Insulation</li><li>Air Cleaners</li><li>Humidifiers</li><li>Duct</li>
  </ul>
</div>

<section class="sec hero" role="img" aria-label="Suburban home with a branded service van parked in the driveway">
  <div class="abs hero-box">
    <h1>We Are An Air Conditioning &amp; Heating Business Serving Residential &amp; Commercial Clients</h1>
    <span class="btn btn-navy" style="left:10px;top:164px">Get Started <span class="arr"><svg width="10" height="10" viewBox="0 0 10 10"><path d="M3 1l4 4-4 4" stroke="#163c63" stroke-width="2" fill="none"/></svg></span></span>
  </div>
  <div class="abs dots"><i class="on"></i><i></i><i></i></div>
</section>

<section class="sec welcome">
  <h2 class="title" style="top:46px">Welcome to <em>Brovik Climate Services</em></h2>
  <p class="lorem">Lorem ipsum dolor sit amet, consectetuer adipiscing elit, sed diam nonummy nibh euismod tincidunt ut laoreet dolore magna aliquam erat volutpat. Ut wisi enim ad minim veniam, quis nostrud exerci tation ullamcorper suscipit lobortis nisl ut aliquip ex ea commodo consequat. Duis autem vel eum iriure dolor in hendrerit in vulputate velit esse molestie consequat, vel illum dolore eu feugiat nulla facilisis at vero eros et accumsan et iusto odio dignissim qui blandit praesent luptatum zzril delenit augue duis dolore te feugait nulla facilisi.</p>
  <span class="btn btn-red" style="left:520px;top:248px">Read More <span class="arr"><svg width="10" height="10" viewBox="0 0 10 10"><path d="M3 1l4 4-4 4" stroke="#c9252c" stroke-width="2" fill="none"/></svg></span></span>
</section>

<section class="sec services">
  <div class="tab"></div>
  <h2 class="title" style="top:10px">Our Services</h2>

  <div class="svc" style="left:82px;top:100px"><div class="ic"><svg width="56" height="40" viewBox="0 0 56 40" fill="none" stroke="#1c5a8f" stroke-width="3"><rect x="2" y="4" width="52" height="20" rx="3"/><path d="M8 18h40M16 30v6M28 30v8M40 30v6"/></svg></div><div><h3>Air Conditioning</h3><p>Lorem ipsum dolor sit amet, consectetuer adipiscing elit, sed diam nonummy nibh euismod tincidunt ut laoreet dolore magna aliquam erat volutpat.</p></div></div>
  <div class="svc" style="left:628px;top:100px"><div class="ic"><svg width="50" height="50" viewBox="0 0 50 50" fill="none" stroke="#1c5a8f" stroke-width="3"><rect x="6" y="18" width="38" height="26" rx="3"/><path d="M14 18v26M22 18v26M30 18v26M38 18v26M14 4c3 3-3 6 0 9M25 4c3 3-3 6 0 9M36 4c3 3-3 6 0 9"/></svg></div><div><h3>Heating</h3><p>Lorem ipsum dolor sit amet, consectetuer adipiscing elit, sed diam nonummy nibh euismod tincidunt ut laoreet dolore magna aliquam erat volutpat.</p></div></div>

  <div class="svc" style="left:82px;top:260px"><div class="ic"><svg width="30" height="56" viewBox="0 0 30 56" fill="none" stroke="#1c5a8f" stroke-width="3"><path d="M9 36V8a6 6 0 0 1 12 0v28a10 10 0 1 1-12 0z"/><circle cx="15" cy="44" r="4" fill="#c9252c" stroke="none"/><path d="M15 40V18" stroke="#c9252c"/></svg></div><div><h3>Thermostats</h3><p>Lorem ipsum dolor sit amet, consectetuer adipiscing elit, sed diam nonummy nibh euismod tincidunt ut laoreet dolore magna aliquam erat volutpat.</p></div></div>
  <div class="svc" style="left:628px;top:260px"><div class="ic"><svg width="50" height="50" viewBox="0 0 50 50" fill="#23865a"><circle cx="25" cy="25" r="5"/><ellipse cx="25" cy="10" rx="5" ry="9"/><ellipse cx="25" cy="40" rx="5" ry="9"/><ellipse cx="10" cy="25" rx="9" ry="5"/><ellipse cx="40" cy="25" rx="9" ry="5"/></svg></div><div><h3>Heat Pump</h3><p>Lorem ipsum dolor sit amet, consectetuer adipiscing elit, sed diam nonummy nibh euismod tincidunt ut laoreet dolore magna aliquam erat volutpat.</p></div></div>

  <div class="svc" style="left:82px;top:422px"><div class="ic"><svg width="54" height="54" viewBox="0 0 54 54"><circle cx="27" cy="27" r="25" fill="#23865a"/><g fill="#fff"><ellipse cx="27" cy="15" rx="6" ry="10"/><ellipse cx="17" cy="34" rx="10" ry="6" transform="rotate(30 17 34)"/><ellipse cx="37" cy="34" rx="10" ry="6" transform="rotate(-30 37 34)"/></g><circle cx="27" cy="27" r="4" fill="#23865a"/></svg></div><div><h3>Air Handler</h3><p>Lorem ipsum dolor sit amet, consectetuer adipiscing elit, sed diam nonummy nibh euismod tincidunt ut laoreet dolore magna aliquam erat volutpat.</p></div></div>
  <div class="svc" style="left:628px;top:422px"><div class="ic"><svg width="54" height="54" viewBox="0 0 54 54" fill="none" stroke="#23865a" stroke-width="3"><circle cx="16" cy="18" r="6"/><circle cx="38" cy="36" r="6"/><path d="M6 36c0-6 4-10 10-10s10 4 10 10M28 12h16v10H34l-4 4v-4h-2zM10 42h14"/></svg></div><div><h3>Self Communicating Systems</h3><p>Lorem ipsum dolor sit amet, consectetuer adipiscing elit, sed diam nonummy nibh euismod tincidunt ut laoreet dolore magna aliquam erat volutpat.</p></div></div>

  <span class="btn btn-red" style="left:476px;top:570px">View All Services <span class="arr"><svg width="10" height="10" viewBox="0 0 10 10"><path d="M3 1l4 4-4 4" stroke="#c9252c" stroke-width="2" fill="none"/></svg></span></span>
</section>

<div class="abs" role="img" aria-label="Cartoon technician mascot giving a thumbs up" style="left:940px;top:1532px;width:190px;height:270px;border-radius:40% 40% 10% 10%;background:linear-gradient(180deg,#3d6fa8 0%,#1c5a8f 55%,#1d3550 100%);z-index:2"></div>

<section class="sec satisfy">
  <h2>Your Satisfaction is Guaranteed<br>....Our Reputation Depends on It</h2>
  <span class="btn btn-red" style="left:498px;top:191px">Call Us Today <span class="arr"><svg width="10" height="10" viewBox="0 0 10 10"><path d="M3 1l4 4-4 4" stroke="#c9252c" stroke-width="2" fill="none"/></svg></span></span>
</section>

<section class="sec promo">
  <div class="half" style="left:0;background:linear-gradient(135deg,#2f3338,#4a4e53 50%,#2b2e32)" role="img" aria-label="Dark photo of a hand holding a smartphone with a coupon">
    <div class="circ"><svg width="52" height="52" viewBox="0 0 52 52"><path d="M26 4h20v20L24 46 4 26z" fill="#23865a"/><circle cx="38" cy="13" r="3.5" fill="#fff"/><text x="22" y="31" font-family="Roboto,sans-serif" font-size="14" font-weight="700" fill="#fff" transform="rotate(-45 22 27)">%</text></svg></div>
    <h3>Coupons / Promotions</h3>
    <p>Lorem ipsum dolor sit amet, consectetuer adipiscing elit, sed diam nonummy nibh euismod tincidunt ut laoreet dolore magna aliquam erat volutpat. nibh euismod tincidunt ut laoreet dolore magna.</p>
    <span class="btn btn-green" style="left:226px;top:278px">Get Started <span class="arr"><svg width="10" height="10" viewBox="0 0 10 10"><path d="M3 1l4 4-4 4" stroke="#23865a" stroke-width="2" fill="none"/></svg></span></span>
  </div>
  <div class="half" style="left:600px;background:linear-gradient(135deg,#77797c,#a3a5a8 50%,#6d7073)" role="img" aria-label="Soft grey photo of paperwork and a calculator">
    <div class="circ" style="border-color:var(--blue)"><svg width="52" height="52" viewBox="0 0 52 52"><rect x="8" y="18" width="36" height="26" rx="3" fill="#1c5a8f"/><rect x="16" y="8" width="22" height="14" rx="2" fill="#fff" stroke="#1c5a8f" stroke-width="2"/><circle cx="26" cy="31" r="5" fill="#fff"/></svg></div>
    <h3>Financing</h3>
    <p>Lorem ipsum dolor sit amet, consectetuer adipiscing elit, sed diam nonummy nibh euismod tincidunt ut laoreet dolore magna aliquam erat volutpat. nibh euismod tincidunt ut laoreet dolore magna.</p>
    <span class="btn btn-navy" style="left:226px;top:278px">Get Started <span class="arr"><svg width="10" height="10" viewBox="0 0 10 10"><path d="M3 1l4 4-4 4" stroke="#163c63" stroke-width="2" fill="none"/></svg></span></span>
  </div>
</section>

<section class="sec testi">
  <h2 class="title" style="top:40px;color:var(--green-dark)">Client Testimonials</h2>
  <svg class="abs" style="left:582px;top:124px" width="36" height="30" viewBox="0 0 36 30"><path fill="#c9252c" d="M0 30V16C0 7 5 2 14 0l1 4c-5 2-7 5-7 10h7v16zM21 30V16c0-9 5-14 14-16l1 4c-5 2-7 5-7 10h7v16z"/></svg>
  <p class="lorem">Lorem ipsum dolor sit amet, consectetuer adipiscing elit, sed diam nonummy nibh euismod tincidunt ut laoreet dolore magna aliquam erat volutpat. nibh euismod tincidunt ut laoreet dolore magna.Lorem ipsum dolor sit amet, consectetuer adipiscing elit, sed diam nonummy nibh euismod tincidunt ut laoreet dolore magna aliquam erat volutpat. nibh euismod tincidunt ut laoreet dolore magna.Lorem ipsum dolor sit amet, consectetuer adipiscing elit, sed diam nonummy nibh euismod tincidunt ut laoreet dolore magna aliquam erat volutpat.</p>
  <div class="abs avatar" role="img" aria-label="Client portrait"></div>
  <div class="who">Martin Doyle</div>
  <div class="role">Lorem ipsum dolor</div>
  <div class="abs tdots"><i></i><i></i><i class="off"></i><i></i></div>
</section>

<section class="sec blogs">
  <h2 class="title" style="top:44px">Latest <em>Blogs</em></h2>
  <article class="card" style="left:82px">
    <div class="ph" role="img" aria-label="Technician servicing an outdoor condenser unit" style="background:linear-gradient(160deg,#c8cdd0,#7d8a7a 60%,#556b4f)"></div>
    <div class="date"><b>26</b>Oct<br>2016</div>
    <h4>LOREM IPSUM DOLOR</h4>
    <p>Sed ut perspiciatis unde omnis iste natus luptatem accusa ni ium doloreom que laudantium totam rem aperiam laudantium.</p>
    <div class="meta"><b>By :</b> Sed ut perspiciatis &nbsp;|&nbsp; <b>0</b> Comments</div>
  </article>
  <article class="card" style="left:438px">
    <div class="ph" role="img" aria-label="Technician checking refrigerant gauges on an AC unit" style="background:linear-gradient(160deg,#9aa7b1,#5f6f7e 55%,#8b8f8a)"></div>
    <div class="date"><b>26</b>Oct<br>2016</div>
    <h4>LOREM IPSUM DOLOR</h4>
    <p>Sed ut perspiciatis unde omnis iste natus luptatem accusa ni ium doloreom que laudantium totam rem aperiam laudantium.</p>
    <div class="meta"><b>By :</b> Sed ut perspiciatis &nbsp;|&nbsp; <b>0</b> Comments</div>
  </article>
  <article class="card" style="left:788px">
    <div class="ph" role="img" aria-label="Two workers in hard hats inspecting equipment" style="background:linear-gradient(160deg,#a8b3bc,#6c7985 50%,#c9a86a)"></div>
    <div class="date"><b>26</b>Oct<br>2016</div>
    <h4>LOREM IPSUM DOLOR</h4>
    <p>Sed ut perspiciatis unde omnis iste natus luptatem accusa ni ium doloreom que laudantium totam rem aperiam laudantium.</p>
    <div class="meta"><b>By :</b> Sed ut perspiciatis &nbsp;|&nbsp; <b>0</b> Comments</div>
  </article>
</section>

<footer class="sec footer" role="contentinfo">
  <div class="fc" style="left:146px">
    <div class="line" style="left:6px"></div><div class="line" style="right:6px"></div>
    <svg width="18" height="24" viewBox="0 0 18 24"><path d="M9 1a8 8 0 0 0-8 8c0 6 8 14 8 14s8-8 8-14a8 8 0 0 0-8-8z" fill="none" stroke="#fff" stroke-width="1.6"/><circle cx="9" cy="9" r="3" fill="none" stroke="#fff" stroke-width="1.6"/></svg>
    <span>12 Lorem ipsum dolor 456 Sed diam, nonummy</span>
  </div>
  <div class="fc" style="left:450px">
    <div class="line" style="left:6px"></div><div class="line" style="right:6px"></div>
    <svg width="22" height="22" viewBox="0 0 24 24"><path fill="none" stroke="#fff" stroke-width="1.6" d="M6.6 10.8a15 15 0 0 0 6.6 6.6l2.2-2.2c.3-.3.7-.4 1-.2 1.1.4 2.3.6 3.6.6.6 0 1 .4 1 1V20c0 .6-.4 1-1 1A17 17 0 0 1 3 4c0-.6.4-1 1-1h3.5c.6 0 1 .4 1 1 0 1.3.2 2.5.6 3.6.1.3 0 .7-.2 1z"/></svg>
    <span>Phone: +61 400 555 218</span>
  </div>
  <div class="fc" style="left:746px">
    <div class="line" style="left:6px"></div>
    <svg width="22" height="22" viewBox="0 0 24 24"><path fill="none" stroke="#fff" stroke-width="1.6" d="M2 11l20-9-9 20-2-9z"/></svg>
    <span>Email: office@brovikclimate.com</span>
  </div>
  <div class="abs" role="img" aria-label="Faint mascot and company badge emblem" style="left:540px;top:129px;width:120px;height:167px;border-radius:40% 40% 10% 10%;background:linear-gradient(180deg,rgba(255,255,255,.35),rgba(255,255,255,.12))"></div>
  <div class="fnav"><span>Home</span><span>About Us</span><span>Services</span><span>Blog</span><span>Financing</span><span>Testimonials</span><span>Contact Us</span></div>
  <div class="abs frule"></div>
  <div class="abs copy">Copyright © 2016 Brovik Climate Services. All Right Reserved.</div>
  <div class="abs social"><i></i><i></i><i></i><i class="r"></i></div>
</footer>

</body>
</html>
```